rose gold typography style landscape business card | upmarket tanning lounge

After years of receiving spray tans, we are two young professionals starting our own spray tanning business. Our point of difference is offering a complete tanning experience within a fun, edgy yet professional atmosphere.
Our ideal card would draw upon design elements from the typography example we have attached. We are hoping to have "velmira" in all lowercase in the typography style, with "TANNING LOUNGE" in much smaller uppercase font underneath but closely positioned below "velmira".
We have attached an example of a business card created by a designer on here - we like how the word on the front almost goes beyond the edges of the card itself.
But you have the design know how, so please let your creative juices flow!
We are thinking either rose gold text (matte rather than a chrome look) with a white background or rose gold freehand style typography with a charcoal background using landscape orientation. We have opted for a thicker style edgy typography to accommodate the metallic look font we are looking for.
We cannot wait to see what you create! Thanks in advance.
Harriet & Josephine
Updates
Project Deadline Extended
Reason: Firstly, we wish to thank each and every one of you who have provided a submission for our project. You guys are amazingly talented and we've loved watching all the designs come through.
We have decided to take our top four favourite designs to a poll with our friends and family and will therefore need to extend the deadline by a couple of days.
We do apologise for any inconvenience this may have caused and thank you for your patience and understanding!
Harriet & Josephine
Industry/Entity Type
Business
Look and feel
Each slider illustrates characteristics of the customer's brand and the style your logo design should communicate.

```html
<!DOCTYPE html>
<html lang="en">
<head>
<meta charset="utf-8">
<title>velmira tanning lounge – business card options</title>
<link rel="stylesheet" href="https://fonts.googleapis.com/css2?family=Quicksand:wght@500;600&family=Lato:wght@400&display=swap">
<style>
  :root {
    --backdrop-top: #b9bcbc;
    --backdrop-bottom: #8f9393;
    --card-white: #ffffff;
    --rose-gold-matte: #b8735a;
    --rose-gold-bright: #e88a6c;
    --ink-grey: #6f6f6f;
    --label-white: #ffffff;
  }
  * { margin: 0; padding: 0; box-sizing: border-box; }
  html, body {
    width: 893px;
    height: 1200px;
    overflow: hidden;
  }
  body {
    background: linear-gradient(180deg, var(--backdrop-top), var(--backdrop-bottom));
    font-family: "Quicksand", sans-serif;
    position: relative;
  }
  .business-card {
    position: absolute;
    left: 146px;
    width: 600px;
    height: 345px;
    background: var(--card-white);
    box-shadow: 0 14px 30px rgba(0, 0, 0, 0.28);
    overflow: hidden;
  }
  .business-card--option-one { top: 70px; --accent: var(--rose-gold-matte); }
  .business-card--option-two { top: 700px; --accent: var(--rose-gold-bright); }

  .brand-name {
    position: absolute;
    left: 54px;
    top: 70px;
    font-family: "Quicksand", sans-serif;
    font-weight: 600;
    font-size: 112px;
    line-height: 1;
    letter-spacing: -1px;
    color: var(--accent);
  }
  .brand-tagline {
    position: absolute;
    left: 62px;
    top: 200px;
    font-family: "Quicksand", sans-serif;
    font-weight: 600;
    font-size: 15px;
    letter-spacing: 1.5px;
    color: var(--accent);
  }
  .contact-block {
    position: absolute;
    left: 380px;
    top: 202px;
    color: var(--ink-grey);
    font-family: "Lato", sans-serif;
  }
  .contact-names {
    font-size: 15px;
    margin-bottom: 8px;
  }
  .contact-phone {
    display: flex;
    align-items: center;
    gap: 8px;
    font-size: 15px;
    letter-spacing: 0.5px;
  }
  .contact-phone svg { width: 14px; height: 14px; fill: var(--ink-grey); }

  .option-label {
    position: absolute;
    left: 34px;
    font-family: "Lato", sans-serif;
    font-size: 27px;
    color: var(--label-white);
  }
  .option-label--one { top: 540px; }
  .option-label--two { top: 600px; }
</style>
</head>
<body>

  <section class="business-card business-card--option-one" aria-label="Business card, option 1">
    <h1 class="brand-name">velmira</h1>
    <p class="brand-tagline">TANNING LOUNGE</p>
    <div class="contact-block">
      <p class="contact-names">Harriet &amp; Josephine</p>
      <p class="contact-phone">
        <svg viewBox="0 0 24 24" aria-hidden="true"><path d="M6.6 10.8a15.2 15.2 0 0 0 6.6 6.6l2.2-2.2a1 1 0 0 1 1-.25 11.4 11.4 0 0 0 3.6.57 1 1 0 0 1 1 1V20a1 1 0 0 1-1 1A17 17 0 0 1 3 4a1 1 0 0 1 1-1h3.5a1 1 0 0 1 1 1 11.4 11.4 0 0 0 .57 3.6 1 1 0 0 1-.25 1z"/></svg>
        0044455566
      </p>
    </div>
  </section>

  <p class="option-label option-label--one">Option 1</p>
  <p class="option-label option-label--two">Option 2</p>

  <section class="business-card business-card--option-two" aria-label="Business card, option 2">
    <h2 class="brand-name">velmira</h2>
    <p class="brand-tagline">TANNING LOUNGE</p>
    <div class="contact-block">
      <p class="contact-names">Harriet &amp; Josephine</p>
      <p class="contact-phone">
        <svg viewBox="0 0 24 24" aria-hidden="true"><path d="M6.6 10.8a15.2 15.2 0 0 0 6.6 6.6l2.2-2.2a1 1 0 0 1 1-.25 11.4 11.4 0 0 0 3.6.57 1 1 0 0 1 1 1V20a1 1 0 0 1-1 1A17 17 0 0 1 3 4a1 1 0 0 1 1-1h3.5a1 1 0 0 1 1 1 11.4 11.4 0 0 0 .57 3.6 1 1 0 0 1-.25 1z"/></svg>
        0044455566
      </p>
    </div>
  </section>

</body>
</html>
```